Business Card for Marriage Commissioner

I am a marriage commissioner in the province of Alberta, meaning that I perform civil unions here. I have been trying to think of a unique design for my business card, something a bit different. A lot of "unique" designs seem to incorporate unique cuts or "some assembly required" or printed on plastic or meat. I would like my design to be a full colour card that is a typical business card size.

The information on the card should have:
Lou Varnik
my occupation: Marriage Commissioner
my website: www.louvarnik.ca
my e-mail: lou@louvarnik.ca
my phone: 780-418-2964

I originally submitted a design to the printer that had a screen capture of a findly search window, with my name and occupation in the text box. And underneath that, my phone number. Nothing else. They indicated they could not print this because it was a copyright violation.

One option on the design is I am a retired chemist-so a chemistry themed card would also be of interest, as long as it isn't a "Rusted Tide" theme, as I have that on my other business cards already...

I would prefer a single sided card, but I am open to a double sided card if it is clever!

I would also prefer not to have pictures of male and female couples as in my position I will also marry same sex couples. Same thing for male/female symbols. Someone has submitted two graduated cylinders in love, which is very clever, and gets around this male/female type.

Thanks for your help and interest.

Target Market(s)

Young couples.

Industry/Entity Type

Plastic

Requirements
Nice to have
• chemistry ideas!
Should not have
• Male/female pictures, male/female symbols.
No QR codes.
No transparent designs, will go on paper stock.

```html
<!DOCTYPE html>
<html lang="en">
<head>
<meta charset="utf-8">
<title>Lou Varnik – Marriage Commissioner Business Card</title>
<link rel="stylesheet" href="https://fonts.googleapis.com/css2?family=Lato:wght@300;400;700;900&display=swap">
<style>
  :root {
    --backdrop: #e9e9e9;
    --card-dark: #333333;
    --card-light: #ffffff;
    --accent-blue: #2aa6df;
    --muted-grey: #9b9b9b;
    --ink: #111111;
    --icon-ink: #333333;
  }
  * { box-sizing: border-box; margin: 0; padding: 0; }
  html, body {
    width: 1200px;
    height: 900px;
    overflow: hidden;
    background: var(--backdrop);
    font-family: "Lato", sans-serif;
  }
  .stage {
    position: relative;
    width: 1200px;
    height: 900px;
  }
  .card {
    position: absolute;
    left: 300px;
    width: 600px;
    height: 343px;
    background: var(--card-dark);
  }
  .card--back {
    top: 70px;
    clip-path: polygon(0 0, 586px 0, 586px 58px, 600px 76px, 600px 343px, 0 343px);
  }
  .card--front {
    top: 480px;
    clip-path: polygon(0 0, 600px 0, 600px 343px, 14px 343px, 14px 262px, 0 244px);
  }

  /* Back */
  .back-identity {
    position: absolute;
    left: 0;
    right: 0;
    top: 128px;
    text-align: center;
    color: var(--muted-grey);
  }
  .back-identity__name {
    font-weight: 400;
    font-size: 40px;
    line-height: 1.1;
  }
  .back-identity__title {
    margin-top: 6px;
    font-weight: 400;
    font-size: 14px;
    letter-spacing: 1px;
  }

  /* Front */
  .front-split {
    position: absolute;
    inset: 0;
    width: 600px;
    height: 343px;
  }
  .front-identity {
    position: absolute;
    left: 62px;
    top: 236px;
  }
  .front-identity__name {
    font-weight: 900;
    font-size: 24px;
    line-height: 1.05;
    color: var(--accent-blue);
  }
  .front-identity__role {
    font-weight: 300;
    font-size: 18px;
    line-height: 1.2;
    color: var(--card-light);
  }
  .contact-list {
    position: absolute;
    left: 360px;
    top: 0;
    list-style: none;
  }
  .contact-list__item {
    position: absolute;
    left: 0;
    white-space: nowrap;
    font-size: 15px;
    line-height: 18px;
    color: var(--ink);
  }
  .contact-list__item--phone { top: 101px; }
  .contact-list__item--email { top: 147px; }
  .contact-list__item--web   { top: 193px; }
  .contact-icon {
    position: absolute;
    left: 272px;
    width: 28px;
    height: 28px;
  }
  .contact-icon--phone { top: 97px; }
  .contact-icon--email { top: 143px; }
  .contact-icon--web   { top: 189px; }
</style>
</head>
<body>
<main class="stage">

  <section class="card card--back" aria-label="Card back">
    <div class="back-identity">
      <p class="back-identity__name">Lou Varnik</p>
      <p class="back-identity__title">Alberta Marriage Commissioner</p>
    </div>
  </section>

  <section class="card card--front" aria-label="Card front">
    <svg class="front-split" viewBox="0 0 600 343" aria-hidden="true">
      <polygon fill="var(--card-light)"
        points="330,0 600,0 600,343 330,343
                330,230 306,216 330,202
                330,184 306,170 330,156
                330,138 306,124 330,110"/>
    </svg>

    <svg class="contact-icon contact-icon--phone" viewBox="0 0 28 28" aria-hidden="true">
      <circle cx="14" cy="14" r="14" fill="var(--card-light)"/>
      <path fill="var(--icon-ink)" d="M9.2 7.5l2.2-.6 1.4 3.2-1.4 1.1c.7 1.7 2 3 3.6 3.7l1.1-1.4 3.2 1.4-.6 2.2c-.2.6-.8 1-1.5.9-4.6-.6-8.2-4.2-8.8-8.8-.1-.7.3-1.3.8-1.7z"/>
    </svg>
    <svg class="contact-icon contact-icon--email" viewBox="0 0 28 28" aria-hidden="true">
      <circle cx="14" cy="14" r="14" fill="var(--card-light)"/>
      <rect x="7" y="9" width="14" height="10" fill="var(--icon-ink)"/>
      <polyline points="7,9 14,15 21,9" fill="none" stroke="var(--card-light)" stroke-width="1.2"/>
    </svg>
    <svg class="contact-icon contact-icon--web" viewBox="0 0 28 28" aria-hidden="true">
      <circle cx="14" cy="14" r="14" fill="var(--card-light)"/>
      <g fill="none" stroke="var(--icon-ink)" stroke-width="1.3">
        <circle cx="14" cy="14" r="7"/>
        <ellipse cx="14" cy="14" rx="3" ry="7"/>
        <line x1="7" y1="14" x2="21" y2="14"/>
        <line x1="8" y1="10.5" x2="20" y2="10.5"/>
        <line x1="8" y1="17.5" x2="20" y2="17.5"/>
      </g>
    </svg>

    <ul class="contact-list">
      <li class="contact-list__item contact-list__item--phone">780-418-2964</li>
      <li class="contact-list__item contact-list__item--email">lou@louvarnik.ca</li>
      <li class="contact-list__item contact-list__item--web">www.louvarnik.ca</li>
    </ul>

    <div class="front-identity">
      <p class="front-identity__name">Lou Varnik</p>
      <p class="front-identity__role">Marriage Commissioner</p>
    </div>
  </section>

</main>
</body>
</html>
```